Zenfro loop flyer

I want this flyer to look like the one I upload here called zenfro loop. I want the to change to words (headline):"A new category in pet hydration" to: Ny unik produkt i Kategori hund. Also remove Functional elektrodryck för hundar.
Also change:" Vi tar emot Återförsäljarpartners" to "Kontakta oss för mer information"
If you think or see improvments plase do so. Its for a launch of a newe product to retailers (so not to the consumer).

Target Market(s)

Retail, stores, hotels, restaurants

Industry/Entity Type

Energy water for dogs

Colors
0054AA
0677BA
7BADD7
CADEEF
E8F1F8

Requirements
Must have
• Think grimvolt, quorza pell, energy drinks but for dogs

```html
<!DOCTYPE html>
<html lang="sv">
<head>
<meta charset="utf-8">
<title>Zenfro loop – Flyer</title>
<link rel="stylesheet" href="https://fonts.googleapis.com/css2?family=Bebas+Neue&family=Poppins:wght@400;500;600;700&display=swap">
<style>
  :root {
    --navy: #0b0f72;
    --gold: #b89a55;
    --red: #9b1c22;
    --card: #dfe2e6;
    --rule: #d4d6da;
    --stage: #ececec;
    --cap: #1b1b1b;
    --clear: #e6edf3;
    --blue-1: #0054aa;
    --blue-2: #0677ba;
    --blue-3: #7badd7;
    --blue-4: #cadeef;
    --blue-5: #e8f1f8;
  }
  * { box-sizing: border-box; margin: 0; padding: 0; }
  html, body { width: 999px; height: 1200px; overflow: hidden; }
  body { background: var(--stage); font-family: "Poppins", sans-serif; color: var(--navy); }
  .flyer { position: absolute; left: 96px; top: 30px; width: 806px; height: 1140px; background: linear-gradient(90deg, #fbfbfb, #eef0f0); overflow: hidden; }
  .abs { position: absolute; }

  .brand { left: 60px; top: 96px; display: flex; align-items: center; gap: 10px; }
  .brand-mark { width: 22px; height: 22px; background: #111; }
  .brand-name { font-size: 27px; font-weight: 700; color: #111; line-height: 1; }
  .brand-divider { left: 273px; top: 90px; width: 2px; height: 53px; background: #111; }
  .tagline { left: 302px; top: 97px; font-size: 14.5px; font-weight: 500; letter-spacing: 1.6px; line-height: 23px; color: #111; }

  .ribbon { left: 618px; top: 0; width: 127px; height: 188px; }
  .ribbon-text { left: 618px; top: 70px; width: 127px; text-align: center; color: var(--gold); font-size: 15.5px; line-height: 21px; letter-spacing: .5px; }
  .flag { left: 663px; top: 120px; }

  .product-visual { left: 323px; top: 187px; width: 180px; height: 723px; z-index: 0;
    border-radius: 40px 40px 14px 14px;
    background: linear-gradient(180deg, var(--cap) 0 9%, var(--clear) 9% 30%, var(--blue-1) 30% 72%, var(--clear) 72% 100%); }

  .headline { left: 60px; top: 218px; z-index: 2; font-family: "Bebas Neue", sans-serif; font-size: 76px; line-height: 72px; color: var(--navy); }
  .headline .accent { color: var(--gold); display: block; }

  .intro { left: 526px; top: 242px; font-size: 12.5px; line-height: 21px; }
  .intro-rule { left: 526px; top: 296px; width: 50px; height: 2px; background: var(--gold); }
  .feature { left: 526px; display: flex; gap: 10px; width: 230px; }
  .feature-icon { width: 54px; height: 54px; border-radius: 50%; flex: none; display: flex; align-items: center; justify-content: center; }
  .feature h3 { font-size: 11.5px; font-weight: 700; line-height: 18px; margin-top: -4px; }
  .feature p { font-size: 9.5px; line-height: 17px; margin-top: 2px; }
  .feature-rule { left: 526px; width: 210px; height: 1px; background: var(--rule); }

  .category { left: 573px; top: 636px; width: 172px; height: 237px; background: var(--card); border-radius: 14px; padding: 24px 17px; z-index: 2; }
  .category h3 { font-size: 11.5px; font-weight: 700; }
  .category .rule { width: 28px; height: 2px; background: var(--gold); margin: 8px 0 10px; }
  .category p { font-size: 9px; line-height: 16px; }
  .category .chart { margin: 18px 0 12px 4px; }
  .category .note { font-size: 10.5px; line-height: 16px; font-weight: 500; }

  .retail-panel { left: 0; top: 538px; width: 290px; height: 348px; z-index: 2; background: var(--navy); border-radius: 0 22px 22px 0; color: #fff; padding: 19px 0 0 60px; }
  .retail-panel h2 { font-size: 13.5px; font-weight: 600; line-height: 19px; }
  .retail-panel .rule { width: 188px; height: 1px; background: var(--gold); margin: 10px 0 13px; }
  .reason { display: flex; gap: 8px; margin-bottom: 17px; }
  .reason-icon { width: 46px; height: 46px; border-radius: 50%; background: var(--gold); flex: none; display: flex; align-items: center; justify-content: center; }
  .reason h4 { font-size: 9.5px; font-weight: 400; line-height: 13px; }
  .reason p { font-size: 8.5px; line-height: 13px; margin-top: 2px; }

  .footer { left: 0; top: 931px; width: 806px; height: 209px; background: var(--navy); z-index: 1; }
  .banner { left: 61px; top: 912px; width: 685px; height: 38px; z-index: 3; background: var(--gold); border-radius: 14px; display: flex; align-items: center; justify-content: center; font-size: 14px; font-weight: 700; color: var(--navy); letter-spacing: .2px; }
  .contact-title { left: 60px; top: 993px; z-index: 3; font-family: "Bebas Neue", sans-serif; font-size: 50px; line-height: 50px; color: #fff; }
  .contact-sub { left: 60px; top: 1052px; z-index: 3; font-size: 13.5px; color: #fff; letter-spacing: .3px; }
  .v-rule { top: 980px; width: 2px; height: 100px; background: var(--gold); z-index: 3; }
  .contact-list { left: 342px; top: 990px; z-index: 3; list-style: none; color: #fff; font-size: 12px; }
  .contact-list li { display: flex; align-items: center; gap: 12px; height: 32.5px; }
  .launch { left: 578px; top: 980px; width: 170px; z-index: 3; color: #fff; }
  .launch-label { font-size: 10.5px; text-align: center; white-space: nowrap; }
  .launch-date { margin-top: 8px; height: 32px; background: var(--gold); color: var(--navy); font-size: 16.5px; font-weight: 700; display: flex; align-items: center; justify-content: center; }
  .launch p { font-size: 11.5px; line-height: 19px; margin: 9px 0 0 12px; }
</style>
</head>
<body>
<main class="flyer">

  <div class="abs brand"><span class="brand-mark"></span><span class="brand-name">zenfro loop</span></div>
  <div class="abs brand-divider"></div>
  <p class="abs tagline">FUNCTIONAL HYDRATION<br>FÖR HUNDAR</p>

  <svg class="abs ribbon" viewBox="0 0 127 188"><path d="M0 0H127V188L63.5 164L0 188Z" fill="var(--navy)"/></svg>
  <p class="abs ribbon-text">TILLVERKAD I<br>SVERIGE</p>
  <svg class="abs flag" width="39" height="24" viewBox="0 0 39 24"><rect width="39" height="24" fill="#0a5bc4"/><rect x="11" width="6" height="24" fill="#f6c516"/><rect y="9" width="39" height="6" fill="#f6c516"/></svg>

  <div class="abs product-visual" role="img" aria-label="Produktfoto: 500 ml flaska elektrolytdryck för hundar med blå etikett och vattenstänk"></div>

  <h1 class="abs headline">NY UNIK<br>PRODUKT<span class="accent">I KATEGORI<br>HUND</span></h1>

  <p class="abs intro">Utvecklad för alla hundar.<br>Inspirerad av human sportdryck.</p>
  <div class="abs intro-rule"></div>

  <div class="abs feature" style="top:323px">
    <div class="feature-icon" style="background:var(--navy)">
      <svg width="30" height="30" viewBox="0 0 30 30" fill="none" stroke="#fff" stroke-width="1.5"><path d="M15 3C10 10 7 14 7 18a8 8 0 0 0 16 0c0-4-3-8-8-15Z"/><path d="M16 11l-4 7h4l-2 6 5-8h-4l2-5Z"/></svg>
    </div>
    <div><h3>NATURLIGA<br>ELEKTROLYTER</h3><p>Återställer vätska<br>och stödjer balansen.</p></div>
  </div>
  <div class="abs feature-rule" style="top:404px"></div>

  <div class="abs feature" style="top:424px">
    <div class="feature-icon" style="background:var(--red)">
      <svg width="30" height="30" viewBox="0 0 30 30" fill="none" stroke="#fff" stroke-width="1.4"><path d="M15 6c-3 4-4 6-4 8a4 4 0 0 0 8 0c0-2-1-4-4-8Z"/><path d="M9 5c-1.5 2-2 3-2 4a2 2 0 0 0 4 0c0-1-.5-2-2-4Z"/><path d="M21 5c-1.5 2-2 3-2 4a2 2 0 0 0 4 0c0-1-.5-2-2-4Z"/><ellipse cx="15" cy="21" rx="11" ry="4"/></svg>
    </div>
    <div><h3>STÖDJER HYDRERING<br>&amp; ÅTERHÄMTNING</h3><p>Hjälper till att upprätthålla<br>prestationsförmåga<br>och välmående.</p></div>
  </div>
  <div class="abs feature-rule" style="top:519px"></div>

  <div class="abs feature" style="top:536px">
    <div class="feature-icon" style="background:var(--gold)">
      <svg width="34" height="20" viewBox="0 0 34 20" fill="none" stroke="#fff" stroke-width="1.5"><path d="M1 11h8l3-8 4 15 4-12 2 5h11"/></svg>
    </div>
    <div><h3>PERFEKT EFTER AKTIVITET,<br>VÄRME &amp; RESA</h3><p>För vardagens äventyr och<br>särskilda tillfällen.</p></div>
  </div>

  <section class="abs category">
    <h3>KATEGORIMÖJLIGHET</h3>
    <div class="rule"></div>
    <p>Hudhydrering för hundar är ett outnyttjat segment med stor tillväxtpotential.</p>
    <svg class="chart" width="52" height="48" viewBox="0 0 52 48" fill="var(--navy)"><rect x="2" y="38" width="8" height="10"/><rect x="14" y="32" width="8" height="16"/><rect x="26" y="24" width="8" height="24"/><rect x="38" y="14" width="8" height="34"/><path d="M2 30Q24 24 44 6" fill="none" stroke="var(--navy)" stroke-width="3"/><path d="M38 4l10-2-2 10Z"/></svg>
    <p class="note">VÄXANDE EFTERFRÅGAN<br>I HELA EUROPA</p>
  </section>

  <section class="abs retail-panel">
    <h2>VARFÖR ÅTERFÖRSÄLJARE<br>VÄLJER ZENFRO LOOP</h2>
    <div class="rule"></div>
    <div class="reason">
      <div class="reason-icon"><svg width="26" height="22" viewBox="0 0 26 22" fill="none" stroke="var(--navy)" stroke-width="2"><path d="M2 20h22M3 15l6-6 4 4 9-9M17 4h5v5"/></svg></div>
      <div><h4>HÖG MARGINAL.<br>LITEN KONKURRENS</h4><p>Var först på en växande<br>kategori.</p></div>
    </div>
    <div class="reason">
      <div class="reason-icon"><svg width="24" height="22" viewBox="0 0 24 22" fill="none" stroke="var(--navy)" stroke-width="2"><path d="M1 2h4l3 12h12l2-8H7"/><circle cx="9" cy="19" r="1.6"/><circle cx="18" cy="19" r="1.6"/></svg></div>
      <div><h4>SNABBT VÄXANDE SEGMENT<br>INOM HUNDHÄLSA</h4><p>Stark och ökande efterfrågan<br>från medvetna hundägare.</p></div>
    </div>
    <div class="reason">
      <div class="reason-icon"><svg width="24" height="22" viewBox="0 0 24 22" fill="none" stroke="var(--navy)" stroke-width="2"><path d="M12 20S2 13 2 7a5 5 0 0 1 10-1 5 5 0 0 1 10 1c0 6-10 13-10 13Z"/></svg></div>
      <div><h4>STOR IMPULSKÖPSPOTENTIAL</h4><p>Perfekt att placera vid vatten<br>och snacks.</p></div>
    </div>
    <div class="reason">
      <div class="reason-icon"><svg width="24" height="24" viewBox="0 0 24 24" fill="none" stroke="var(--navy)" stroke-width="2"><path d="M13 2h9v9L11 22 2 13Z"/><circle cx="17" cy="7" r="1.5"/></svg></div>
      <div><h4>PREMIUMPOSITIONERING<br>= HÖGRE KUNDVÄRDE</h4><p>Ger mer värde i varje besök.</p></div>
    </div>
  </section>

  <div class="abs footer"></div>
  <div class="abs banner">RENA INGREDIENSER. VERKLIGA FÖRDELAR. HUNDAR KÄNNER SKILLNADEN.</div>

  <h2 class="abs contact-title">KONTAKTA OSS</h2>
  <p class="abs contact-sub">FÖR MER INFORMATION</p>
  <div class="abs v-rule" style="left:303px"></div>
  <ul class="abs contact-list">
    <li><svg width="14" height="16" viewBox="0 0 14 16" fill="none" stroke="#fff" stroke-width="1.5"><rect x="3" y="1" width="8" height="14" rx="1.5"/><path d="M6 12.5h2"/></svg>+46 70 123 45 67</li>
    <li><svg width="14" height="16" viewBox="0 0 14 16"><rect x="0" y="3" width="14" height="10" fill="#fff"/><path d="M0 3l7 6 7-6" fill="none" stroke="var(--navy)" stroke-width="1.4"/></svg>info@zenfroloop.com</li>
    <li><svg width="14" height="16" viewBox="0 0 14 14" fill="none" stroke="#fff" stroke-width="1.3"><circle cx="7" cy="7" r="6"/><ellipse cx="7" cy="7" rx="2.6" ry="6"/><path d="M1 7h12M2 4h10M2 10h10"/></svg>zenfroloop.com</li>
  </ul>
  <div class="abs v-rule" style="left:533px"></div>
  <div class="abs launch">
    <p class="launch-label">— BEGRÄNSAD LANSERING —</p>
    <div class="launch-date">SOMMAREN 2026</div>
    <p>Säkra din tilldelning<br>I tid och möt efterfrågan.</p>
  </div>

</main>
</body>
</html>
```